Pest control

Pest solutions to all residential and commercial sites, the technicians name will be displayed on the back of the card, and a description of his duties: Pest Technician, Termite Inspector,
Termite protection of properties.
The colours will be all white with VORNO and the 1300 582 417 be a blue.
The file with the phone icon is from my web site.
Industry/Entity Type
Residential
Contact Information for Business Card
VORNO PEST SOLUTIONS, 1300 582 417
vorno.com.au
info@vorno.com.au

```html
<!DOCTYPE html>
<html lang="en">
<head>
<meta charset="utf-8">
<title>Vorno Pest Solutions – Business Card</title>
<link href="https://fonts.googleapis.com/css2?family=Exo+2:wght@400;500;700;800&display=swap" rel="stylesheet">
<style>
  :root {
    --bg: #8f8f8f;
    --card: #f4f4f4;
    --blue: #4a68b2;
    --ink: #1e1e1e;
  }
  * { margin: 0; padding: 0; box-sizing: border-box; }
  html, body { width: 1200px; height: 894px; overflow: hidden; }
  body {
    background: var(--bg);
    font-family: "Exo 2", sans-serif;
    display: flex;
    align-items: center;
    justify-content: center;
    gap: 36px;
  }
  .card {
    position: relative;
    width: 540px;
    height: 310px;
    background: var(--card);
    overflow: hidden;
  }
  .band {
    position: absolute;
    right: 0;
    background: var(--blue);
    border-radius: 999px 0 0 999px;
  }

  /* Back side */
  .card--back .band { left: 370px; top: 150px; height: 80px; }
  .person { position: absolute; left: 40px; top: 34px; width: 290px; border-bottom: 2px solid var(--blue); padding-bottom: 6px; }
  .person__name { color: var(--blue); font-size: 24px; font-weight: 500; line-height: 1; }
  .person__role { color: var(--ink); font-size: 9px; letter-spacing: 0.5px; text-transform: uppercase; margin-top: 3px; white-space: nowrap; }
  .contacts { position: absolute; left: 40px; top: 100px; display: grid; grid-template-columns: 76px auto; row-gap: 3px; font-size: 15px; }
  .contacts dt { color: var(--blue); }
  .contacts dd { color: var(--ink); }
  .contacts .contacts__phone { color: var(--blue); font-weight: 500; }
  .address { position: absolute; left: 36px; top: 205px; display: flex; align-items: center; gap: 8px; font-size: 14px; color: var(--ink); white-space: nowrap; }
  .address svg { width: 14px; height: 18px; }
  .rule { position: absolute; left: 40px; right: 0; height: 2px; background: var(--blue); }
  .rule--one { top: 196px; right: 210px; }
  .rule--two { top: 262px; }
  .rule--three { top: 276px; }

  /* Front side */
  .card--front .band { left: 280px; top: 175px; height: 100px; }
  .brand { position: absolute; left: 80px; top: 62px; }
  .brand__name { color: var(--blue); font-size: 64px; font-weight: 800; line-height: 0.9; letter-spacing: 1px; }
  .brand__tag { color: var(--ink); font-size: 15px; font-weight: 500; letter-spacing: 0.5px; margin-top: 2px; }
</style>
</head>
<body>

  <section class="card card--back" aria-label="Business card back">
    <div class="person">
      <h1 class="person__name">Daniel Hart</h1>
      <p class="person__role">Pest Technician · Termite Inspector</p>
    </div>
    <dl class="contacts">
      <dt>Phone:</dt><dd class="contacts__phone">1300 582 417</dd>
      <dt>Fax:</dt><dd class="contacts__phone">1300 582 417</dd>
      <dt>Email:</dt><dd>info@vorno.com.au</dd>
      <dt>website:</dt><dd>www.vorno.com.au</dd>
    </dl>
    <div class="rule rule--one"></div>
    <p class="address">
      <svg viewBox="0 0 14 18" aria-hidden="true"><path d="M7 0C3.1 0 0 3.1 0 7c0 5 7 11 7 11s7-6 7-11C14 3.1 10.9 0 7 0z" fill="#4a68b2"/><circle cx="7" cy="7" r="2.6" fill="#f4f4f4"/></svg>
      14 Harbour Street, Level 3, Brookvale
    </p>
    <div class="rule rule--two"></div>
    <div class="rule rule--three"></div>
    <div class="band"></div>
  </section>

  <section class="card card--front" aria-label="Business card front">
    <div class="brand">
      <p class="brand__name">VORNO</p>
      <p class="brand__tag">PEST SOLUTIONS</p>
    </div>
    <div class="band"></div>
  </section>

</body>
</html>
```